Fresh Nest Builder Guide needs a new Landing Page

I like to get a landing page or website with 2-3 pages to help target home buyers who are looking to buy homes from builders such as PV Dwellings, Moritz, G.T. Falwick, etc. The landing page/website to be non-cluttered and be able to explain to home buyers that there are many benefits to include me as their buyer's agent when they buy a brand new home from any builders.
I may want to incorporate a short explanation video (animated) on the landing page and then for the viewer to click on a button that will take them to another page where they can search for new homes from different builders.
Target Market(s)
Home buyers looking to buy brand new home from builders such as PV Dwellings, Moritz, G.T. Falwick, etc.
Industry/Entity Type
Real Estate
Number of Pages Required
2 page
Requirements
Must have
- The landing page may have the explanation video at the bottom of the landing page (scrolled down) or there may be a CALL TO ACTION button that takes the viewer to the 2nd page to watch the explanation video. Once they watched the explanation video and are still interested, they can click on another CALL TO ACTION button that will take them to another website that they will be able to search for all the available new homes and register their contact information.
Should not have
- No clutters and no dark colors.

```html
<!DOCTYPE html>
<html lang="en">
<head>
<meta charset="utf-8">
<title>Fresh Nest Builder Guide</title>
<link rel="stylesheet" href="https://fonts.googleapis.com/css2?family=Jost:wght@500;600&family=Lato:wght@400;700;900&display=swap">
<style>
  :root {
    --white: #ffffff;
    --header-band: rgba(255, 255, 255, 0.22);
    --cta: #6d2cf5;
    --footer: #1b1b1b;
    --footer-text: #e9e9e9;
    --warm-light: #f3dcc4;
    --warm-mid: #c99a6e;
    --wall-dark: #3e3a40;
    --wall-mid: #57535a;
    --cool-light: #dfe3e8;
    --floor: #a97a52;
  }
  * { margin: 0; padding: 0; box-sizing: border-box; }
  html, body { width: 1200px; height: 709px; overflow: hidden; }
  body { position: relative; font-family: "Lato", sans-serif; color: var(--white); background: var(--footer); }

  .hero-photo {
    position: absolute; left: 0; top: 0; width: 1200px; height: 665px;
    background:
      linear-gradient(180deg, rgba(0,0,0,0) 75%, rgba(120,80,50,0.45) 100%),
      linear-gradient(90deg,
        var(--warm-light) 0%, var(--warm-mid) 18%, #e7c9aa 32%,
        var(--wall-mid) 37%, var(--wall-dark) 55%, var(--wall-mid) 74%,
        var(--cool-light) 75%, #eef0f3 100%);
  }

  .site-header {
    position: absolute; left: 0; top: 0; width: 1200px; height: 88px;
    background: var(--header-band);
  }
  .brand {
    position: absolute; left: 79px; top: 27px;
    font-family: "Lato", sans-serif; font-weight: 700; font-size: 22px; letter-spacing: 0.5px;
  }
  .menu-toggle { position: absolute; left: 1096px; top: 28px; }

  .hero-title {
    position: absolute; left: 0; width: 1196px; top: 196px; text-align: center;
    font-family: "Jost", sans-serif; font-weight: 600; font-size: 48px; letter-spacing: 1.5px;
  }
  .play-button { position: absolute; left: 565px; top: 282px; }
  .cta-button {
    position: absolute; left: 463px; top: 384px; width: 273px; height: 47px;
    border-radius: 24px; background: var(--cta);
    display: flex; align-items: center; justify-content: center;
    font-weight: 700; font-size: 16px; letter-spacing: 0.4px; text-decoration: none; color: var(--white);
  }

  .site-footer {
    position: absolute; left: 0; top: 665px; width: 1200px; height: 44px;
    background: var(--footer); color: var(--footer-text);
    font-size: 13px; font-weight: 700;
  }
  .copyright { position: absolute; left: 74px; top: 14px; display: flex; align-items: center; gap: 6px; }
  .divider { margin: 0 12px 0 14px; font-weight: 400; opacity: 0.7; }
  .page-code { position: absolute; right: 31px; top: 14px; font-weight: 900; }
</style>
</head>
<body>
  <div class="hero-photo" role="img" aria-label="Bright open-plan living room with tall windows, dark concrete feature wall, grey sofa, arc floor lamp and floating wooden staircase"></div>

  <header class="site-header">
    <div class="brand">FRESH NEST BUILDER GUIDE</div>
    <svg class="menu-toggle" width="31" height="24" viewBox="0 0 31 24" aria-label="Menu">
      <rect x="0" y="0" width="31" height="3.5" fill="#fff"/>
      <rect x="0" y="10" width="31" height="3.5" fill="#fff"/>
      <rect x="0" y="20" width="31" height="3.5" fill="#fff"/>
    </svg>
  </header>

  <h1 class="hero-title">FRESH NEST BUILDER GUIDE</h1>

  <svg class="play-button" width="70" height="70" viewBox="0 0 70 70" aria-label="Play video">
    <circle cx="35" cy="35" r="33.5" fill="none" stroke="rgba(255,255,255,0.75)" stroke-width="2"/>
    <polygon points="28,22 28,48 48,35" fill="#fff"/>
  </svg>

  <a class="cta-button" href="#">SEARCH FOR NEW HOMES</a>

  <footer class="site-footer">
    <div class="copyright">
      <svg width="13" height="13" viewBox="0 0 13 13" aria-hidden="true">
        <circle cx="6.5" cy="6.5" r="5.5" fill="none" stroke="#e9e9e9" stroke-width="1.6"/>
        <path d="M8.4 4.7 A2.4 2.4 0 1 0 8.4 8.3" fill="none" stroke="#e9e9e9" stroke-width="1.5"/>
      </svg>
      <span>2018</span><span class="divider">|</span><span>www.freshnestguide.com</span>
    </div>
    <div class="page-code">M1</div>
  </footer>
</body>
</html>
```